Music teacher for flute, beinning piano and a Chime and Stride class

I would like a QP page where folks could contact me for flute and beginning piano lessons OR for a Chime and Stride class (low-impact exercises, singing, work with drumming/rhythms to alleviate the symptoms of Parkinson's disease.) I have a QP page for the Chime and Stride but not for music lessons.
https://www.pagelinkr.example/ChimeandStrideOakvale
I would want a different url since I am no longer doing this in Roseville, CA but Sacramento, CA

Hello, forgive me for dropping out of contact. Can you tell me if there was a fake QP page created under the username Chime and Stride Birchford? It's surprisingly close to what I offer but it says "Painting class" and other misinformation. Any information would be helpful, thanks. I'd like to switch my username to Chime and Stride Birchford, if possible.

```html
<!DOCTYPE html>
<html lang="en">
<head>
<meta charset="utf-8">
<title>Chime and Stride – Social Media Set</title>
<link href="https://fonts.googleapis.com/css2?family=Montserrat:wght@300;400;600;700&display=swap" rel="stylesheet">
<style>
  :root {
    --page-bg: #f1f1f1;
    --label: #2b2b2b;
    --night: #030304;
    --navy: #031552;
    --charcoal: #222423;
    --white: #ffffff;
    --key-white: #f2f2f2;
    --magenta: #e0138c;
    --violet: #6a1bb8;
    --ink: #1c1c1c;
  }
  * { margin: 0; padding: 0; box-sizing: border-box; }
  html, body { width: 1200px; height: 664px; overflow: hidden; }
  body {
    position: relative;
    background: var(--page-bg);
    font-family: "Montserrat", sans-serif;
  }
  .size-label {
    position: absolute;
    font-size: 12px;
    color: var(--label);
    letter-spacing: 0.3px;
  }
  .artboard {
    position: absolute;
    overflow: hidden;
    box-shadow: 0 3px 10px rgba(0,0,0,0.12);
  }
  .headline {
    position: absolute;
    text-align: center;
    text-transform: uppercase;
    line-height: 1.38;
    white-space: nowrap;
    transform: translateX(-50%);
  }
  .headline .strong { font-weight: 600; }
  .headline .light { font-weight: 300; }
  .headline .bold { font-weight: 700; }

  /* Profile square */
  .profile { left: 461px; top: 60px; width: 107px; height: 107px; background: var(--white); }
  .profile .notes-art {
    position: absolute; left: 0; top: 0; width: 107px; height: 56px;
    background: linear-gradient(100deg, #e9366f 0%, #f6a33a 30%, #7a3fb8 55%, #1aa37e 80%, #e23c5a 100%);
    opacity: 0.75;
    -webkit-mask: linear-gradient(#000 40%, transparent);
            mask: linear-gradient(#000 40%, transparent);
  }
  .profile .brand-name {
    position: absolute; left: 0; width: 100%; top: 73px;
    text-align: center; font-size: 7.5px; font-weight: 700; color: var(--magenta);
  }
  .profile .brand-tagline {
    position: absolute; left: 0; width: 100%; top: 84px;
    text-align: center; font-size: 5px; letter-spacing: 1px; color: var(--ink);
  }

  /* Cover: flute */
  .cover-flute { left: 34px; top: 178px; width: 533px; height: 220px; background: var(--night); }
  .cover-flute .portrait-photo {
    position: absolute; left: 200px; top: 0; width: 333px; height: 220px;
    background: radial-gradient(ellipse 40% 60% at 62% 50%, #4a3a30 0%, #1e1714 45%, var(--night) 80%);
  }
  .cover-flute .headline {
    left: 158px; top: 78px; font-size: 16px;
    background: linear-gradient(90deg, var(--magenta), var(--violet));
    -webkit-background-clip: text; background-clip: text; color: transparent;
  }

  /* Cover: keys */
  .cover-keys { left: 34px; top: 409px; width: 533px; height: 220px; background: var(--navy); }
  .cover-keys .notes-art {
    position: absolute; left: 260px; top: 0; width: 230px; height: 200px;
    background: radial-gradient(ellipse at 50% 40%, rgba(110,40,150,0.35), transparent 70%);
  }
  .cover-keys .keys-art {
    position: absolute; left: 34px; top: 53px; width: 223px; height: 89px;
    background: linear-gradient(90deg, #6fb6e8, #b7a6e6, #f3d23a, #7fd3e6, #f3d23a, #9b8be0, #f3d23a);
  }
  .cover-keys .headline { left: 389px; top: 76px; font-size: 16px; color: var(--white); }

  /* Square post */
  .post { left: 578px; top: 28px; width: 602px; height: 602px; background: var(--charcoal); }
  .post .brand-name {
    position: absolute; left: 496px; top: 72px; transform: translateX(-50%);
    font-size: 12px; font-weight: 700; color: var(--white); white-space: nowrap;
  }
  .post .brand-tagline {
    position: absolute; left: 496px; top: 89px; transform: translateX(-50%);
    font-size: 8px; letter-spacing: 2px; color: var(--white); white-space: nowrap;
  }
  .post .keys-art {
    position: absolute; left: 189px; top: 156px; width: 235px; height: 227px;
    background: linear-gradient(90deg, var(--key-white), #cfcfcf, var(--key-white));
    box-shadow: 0 8px 16px rgba(0,0,0,0.4);
  }
  .post .headline { left: 301px; top: 418px; font-size: 26px; color: var(--white); line-height: 1.39; }
</style>
</head>
<body>
  <span class="size-label" style="left:467px;top:40px">170X170</span>
  <span class="size-label" style="left:34px;top:154px">851X351</span>
  <span class="size-label" style="left:34px;top:632px">851X351</span>
  <span class="size-label" style="left:583px;top:632px">960X960</span>

  <section class="artboard profile">
    <div class="notes-art" role="img" aria-label="Colourful scattered music notes illustration"></div>
    <div class="brand-name">Chime and Stride</div>
    <div class="brand-tagline">FREEDOM OF EXPRESSION</div>
  </section>

  <section class="artboard cover-flute">
    <div class="portrait-photo" role="img" aria-label="Photo of a flutist playing in low light against a black background"></div>
    <h2 class="headline">
      <span class="strong">Using music to improve</span><br>
      <span class="light">the lives of folks with</span><br>
      <span class="bold">Parkinson's disease.</span>
    </h2>
  </section>

  <section class="artboard cover-keys">
    <div class="notes-art" role="img" aria-label="Faint flowing music staff and notes decoration"></div>
    <div class="keys-art" role="img" aria-label="Colourful geometric piano keys illustration"></div>
    <h2 class="headline">
      <span class="strong">Using music to improve</span><br>
      <span class="light">the lives of folks with</span><br>
      <span class="bold">Parkinson's disease.</span>
    </h2>
  </section>

  <section class="artboard post">
    <div class="brand-name">Chime and Stride</div>
    <div class="brand-tagline">FREEDOM OF EXPRESSION</div>
    <div class="keys-art" role="img" aria-label="Scattered black and white piano keys illustration"></div>
    <h2 class="headline">
      <span class="strong">Using music to improve</span><br>
      <span class="light">the lives of folks with</span><br>
      <span class="bold">Parkinson's disease.</span>
    </h2>
  </section>
</body>
</html>
```